Billboard - Cool Garden and Landscape Company (Brand Pack Included)

NEED A PROFESSIONAL BILLBOARD TO ADVERTISE OUR BUSINESS. HAVE MOCKED UP A SAMPLE CONCEPT BUT IT REQUIRES THE ICONS TO BE DEVELOPED TO A PROFESSIONAL STANDARD (I JUST COPIED RANDOM EXAMPLES FROM THE NET)

THE ICONS REPRESENT OUR KEY PRODUCT GROUPS. (These can be redesigned)
BILLBOARD IS 6M X 3M (SEE SPEC FILE ATTACHED) - IMAGE OF THE LOCATION ADDED TO THE FILES.

BRAND GUIDE INCLUDED WITH LOGO FILES

VISIT: https://www.facebook.com/Crew.Moss.Crate/
Web: www.mosscrate.co.nz

Target Market(s)

Commuter traffic - busy road - Billboard site is on the left side approx 400m before our street turn off. Age group 30+ Home owners / Builders

Industry/Entity Type

Garden Supply

Font styles to use
Other font styles liked:
• comfortaa

Requirements
Must have
• No change to our logo or brand
• Next left
• Icons for products as per mock up - note these can be redesigned
Nice to have
• Easy to see at a distance
• Clean
• Simple

```html
<!DOCTYPE html>
<html lang="en">
<head>
<meta charset="utf-8">
<title>Moss Crate Billboard</title>
<link href="https://fonts.googleapis.com/css2?family=Comfortaa:wght@400;600&family=Quicksand:wght@500&family=Oswald:wght@500&family=Montserrat:wght@600;800&display=swap" rel="stylesheet">
<style>
  :root {
    --backdrop: #4a4a4a;
    --board: #ffffff;
    --leaf-green: #2ea84a;
    --sun-orange: #f7920f;
    --ink: #111111;
    --divider: #222222;
  }
  html, body {
    margin: 0;
    width: 1200px;
    height: 1200px;
    overflow: hidden;
    background: var(--backdrop);
  }
  .billboard {
    position: absolute;
    left: 46px;
    top: 323px;
    width: 1108px;
    height: 554px;
    background: var(--board);
    box-shadow: 0 6px 14px rgba(0,0,0,0.35);
  }
  .brand-mark {
    position: absolute;
    left: 218px;
    top: 42px;
    width: 130px;
    height: 130px;
    background: var(--leaf-green);
  }
  .brand-name {
    position: absolute;
    left: 372px;
    top: 38px;
    margin: 0;
    font-family: "Quicksand", sans-serif;
    font-weight: 500;
    font-size: 92px;
    letter-spacing: 1px;
    line-height: 1;
    color: var(--leaf-green);
  }
  .brand-rule {
    position: absolute;
    left: 215px;
    top: 176px;
    width: 290px;
    height: 4px;
    background: var(--sun-orange);
  }
  .tagline {
    position: absolute;
    left: 512px;
    top: 148px;
    margin: 0;
    font-family: "Comfortaa", sans-serif;
    font-weight: 600;
    font-size: 31px;
    letter-spacing: 1px;
    color: var(--sun-orange);
  }
  .product-row {
    position: absolute;
    left: 30px;
    top: 200px;
    width: 1050px;
    height: 165px;
    display: flex;
  }
  .product {
    flex: 1;
    display: flex;
    flex-direction: column;
    align-items: center;
    border-left: 2px solid var(--divider);
    border-image: linear-gradient(to bottom, transparent 30%, var(--divider) 30%) 1;
  }
  .product:first-child { border-left: none; }
  .product-icon {
    width: 90px;
    height: 90px;
    border-radius: 12px;
    background: var(--sun-orange);
  }
  .product-label {
    margin-top: 14px;
    font-family: "Oswald", sans-serif;
    font-weight: 500;
    font-size: 26px;
    line-height: 28px;
    text-align: center;
    text-transform: uppercase;
    color: var(--ink);
    transform: scaleX(0.85);
  }
  .direction-arrow {
    position: absolute;
    left: 38px;
    top: 375px;
    width: 310px;
    height: 112px;
  }
  .direction-text {
    position: absolute;
    left: 100px;
    top: 400px;
    width: 247px;
    height: 62px;
    display: flex;
    align-items: center;
    justify-content: center;
    font-family: "Montserrat", sans-serif;
    font-weight: 800;
    font-size: 37px;
    color: var(--ink);
  }
  .address-band {
    position: absolute;
    left: 357px;
    top: 400px;
    width: 751px;
    height: 62px;
    background: var(--leaf-green);
    display: flex;
    align-items: center;
    justify-content: center;
    font-family: "Montserrat", sans-serif;
    font-weight: 800;
    font-size: 36px;
    color: #ffffff;
    text-transform: uppercase;
  }
  .trade-line {
    position: absolute;
    left: 358px;
    top: 476px;
    margin: 0;
    font-family: "Montserrat", sans-serif;
    font-weight: 600;
    font-size: 24px;
    color: var(--ink);
  }
</style>
</head>
<body>
  <section class="billboard">
    <div class="brand-mark"></div>
    <h1 class="brand-name">MOSSCRATE</h1>
    <div class="brand-rule"></div>
    <p class="tagline">Create Better Gardens</p>

    <div class="product-row">
      <div class="product">
        <div class="product-icon" role="img" aria-label="Campfire icon with flames over logs"></div>
        <div class="product-label">Firewood<br>Fire Pellets</div>
      </div>
      <div class="product">
        <div class="product-icon" role="img" aria-label="Seedling growing from a mound of soil"></div>
        <div class="product-label">Compost<br>Soil + Mulch</div>
      </div>
      <div class="product">
        <div class="product-icon" role="img" aria-label="Stack of balanced decorative stones"></div>
        <div class="product-label">Decorative Stone<br>Aggregates</div>
      </div>
      <div class="product">
        <div class="product-icon" role="img" aria-label="Box trailer side view"></div>
        <div class="product-label">Hire Trailers<br>Delivery</div>
      </div>
    </div>

    <svg class="direction-arrow" viewBox="0 0 310 112" aria-hidden="true">
      <polygon points="0,56 56,0 56,25 310,25 310,87 56,87 56,112" fill="var(--sun-orange)"/>
    </svg>
    <div class="direction-text">NEXT LEFT</div>
    <div class="address-band">84 Fernhill Road (off Tamblyn)</div>
    <p class="trade-line">Garden &amp; Landscape Supplies</p>
  </section>
</body>
</html>
```